Illustrate Something - Image of a wall with a quote

Looking for original art that is a picture of a wall (brick I think, maybe wood) with the the following quote saying

WALL (large, or maybe blended into the wall)
"Wait A Little Longer" (medium text)

some ideas

1) an image of someone spray paint the text - [url removed, login to view]:

2) neat image [url removed, login to view]

3) [url removed, login to view]

```html
<!DOCTYPE html>
<html lang="en">
<head>
<meta charset="utf-8">
<title>Wall — Wait A Little Longer</title>
<link rel="stylesheet" href="https://fonts.googleapis.com/css2?family=Anton&display=swap">
<style>
  :root {
    --wall-light: #8a8278;
    --wall-mid: #5b544c;
    --wall-dark: #1e1b18;
    --floor-light: #3a3632;
    --floor-dark: #0d0c0b;
    --title-ink: #f3f0ea;
    --tagline-ink: #cdbf9f;
  }
  * { margin: 0; padding: 0; box-sizing: border-box; }
  html, body {
    width: 1000px;
    height: 1200px;
    overflow: hidden;
    background: #000;
  }
  .poster {
    position: relative;
    width: 1000px;
    height: 1200px;
    overflow: hidden;
  }
  .brick-wall {
    position: absolute;
    left: 0; top: 0;
    width: 1000px;
    height: 900px;
    background: radial-gradient(ellipse 70% 60% at 55% 35%, var(--wall-light) 0%, var(--wall-mid) 55%, var(--wall-dark) 100%);
  }
  .wood-floor {
    position: absolute;
    left: 0; top: 900px;
    width: 1000px;
    height: 300px;
    background: radial-gradient(ellipse 60% 80% at 50% 0%, var(--floor-light) 0%, var(--floor-dark) 100%);
  }
  .type-layer {
    position: absolute;
    left: 0; top: 0;
    width: 1000px;
    height: 1200px;
  }
  .title {
    font-family: "Anton", sans-serif;
    font-weight: 400;
    font-size: 330px;
    fill: var(--title-ink);
  }
  .tagline {
    font-family: "Anton", sans-serif;
    font-weight: 400;
    font-size: 100px;
    fill: var(--tagline-ink);
  }
</style>
</head>
<body>
  <main class="poster">
    <div class="brick-wall" role="img" aria-label="Photograph of an old weathered brick wall, lit from the centre and fading to dark at the edges"></div>
    <div class="wood-floor" role="img" aria-label="Photograph of dark wooden floorboards receding toward the wall"></div>
    <svg class="type-layer" width="1000" height="1200" viewBox="0 0 1000 1200">
      <text class="title" x="271" y="583" textLength="493" lengthAdjust="spacingAndGlyphs">WALL</text>
      <text class="tagline" x="97" y="1183" textLength="778" lengthAdjust="spacingAndGlyphs">WAIT A LITTLE LONGER</text>
    </svg>
  </main>
</body>
</html>
```